Cosmetic injections clinic needs a fresh looking business card

We need a business card using the supplied logo and color scheme to attract future clients to our clinic. It should be modern and fresh, eye catching and not too busy. Simple and to the point is best. I would like two sided designs with the front indicating address and contact information, and the back in full color with white logo and descriptive information also provided.
Target Market(s)
Clients looking for non surgical beauty enhancements.
Contact Information for Business Card
MeloraSkin
14, 618 Birchmont Way
Larkhaven, Ontario
K2P 7W3
Phone: 587-412-6630
Email: info@meloraskin.com
Requirements
Must have
- -Logo supplied with the name and address of the clinic
- -Back of card in full color with white logo with A small line of text indicating both of the following: Anti aging consultants and cosmetic injectables
- Located inside the Voyager Wellness Group

```html
<!DOCTYPE html>
<html lang="en">
<head>
<meta charset="utf-8">
<title>MeloraSkin – Business Card</title>
<link rel="stylesheet" href="https://fonts.googleapis.com/css2?family=Work+Sans:wght@400;500;600&display=swap">
<style>
  :root {
    --stage: #151515;
    --paper: #ffffff;
    --ink: #333333;
    --purple: #6b4aa5;
    --teal: #22b8a0;
    --pink: #e8449a;
    --dark-card: #1d1d1d;
    --dark-card-light: #3a3a3a;
    --white: #ffffff;
  }
  * { box-sizing: border-box; margin: 0; padding: 0; }
  html, body {
    width: 1200px; height: 897px; overflow: hidden;
    background: var(--stage);
    font-family: "Work Sans", Arial, sans-serif;
  }
  .canvas { position: relative; width: 1200px; height: 897px; }
  .card {
    position: absolute; left: 303px; width: 595px; height: 339px;
  }
  .card-front { top: 92px; background: var(--paper); color: var(--ink); }
  .card-back {
    top: 469px;
    background: radial-gradient(ellipse at 85% 45%, var(--dark-card-light) 0%, var(--dark-card) 60%);
    color: var(--white);
  }
  .brand {
    position: absolute; left: 0; right: 0;
    display: flex; align-items: center; justify-content: center; gap: 12px;
    font-weight: 600; letter-spacing: 0.5px; line-height: 1;
  }
  .brand-dot { border-radius: 50%; flex: none; }
  .card-front .brand { top: 95px; font-size: 34px; color: var(--purple); }
  .card-front .brand-dot { width: 26px; height: 26px; background: var(--purple); }
  .card-back .brand { top: 126px; font-size: 42px; color: var(--white); }
  .card-back .brand-dot { width: 32px; height: 32px; background: var(--white); }
  .color-bar {
    position: absolute; top: 189px; left: 126px; width: 343px; height: 5px;
    display: flex;
  }
  .color-bar span { flex: 1; }
  .color-bar .purple { background: var(--purple); }
  .color-bar .teal { background: var(--teal); }
  .color-bar .pink { background: var(--pink); }
  .contact {
    position: absolute; top: 210px; left: 0; right: 0;
    text-align: center; font-size: 14px; line-height: 20px;
  }
  .contact .address { margin-bottom: 5px; }
  .label-p { color: var(--purple); }
  .label-e { color: var(--teal); }
  .label-w, .accent { color: var(--pink); }
  .divider {
    position: absolute; top: 232px; left: 161px; width: 272px; height: 1px;
    background: var(--white);
  }
  .tagline {
    position: absolute; top: 242px; left: 0; right: 0;
    text-align: center; font-size: 11.5px; letter-spacing: 0.2px;
  }
</style>
</head>
<body>
<div class="canvas">
  <section class="card card-front">
    <div class="brand"><span class="brand-dot"></span>MeloraSkin</div>
    <div class="color-bar"><span class="purple"></span><span class="teal"></span><span class="pink"></span></div>
    <div class="contact">
      <p class="address">14, 618 Birchmont Way Larkhaven, Ontario K2P 7W3</p>
      <p><span class="label-p">P:</span> 587-412-6630 | <span class="label-e">E:</span> info@meloraskin.com</p>
      <p><span class="label-w">W:</span> www.<span class="accent">meloraskin</span>.com</p>
    </div>
  </section>
  <section class="card card-back">
    <div class="brand"><span class="brand-dot"></span>MeloraSkin</div>
    <div class="divider"></div>
    <p class="tagline">Anti aging consultants and cosmetic injectables</p>
  </section>
</div>
</body>
</html>
```